Bi-Lingual Trash and Recycle Sign

Hello,

Pretty straight forward. I have not been able to find the exact sign we need for a property with trash and recycle guidelines. I've found close, but not complete. We are looking to have metal 12x18 street sign type signs made to provide these instructions. Attached is a sample taken from the web. I want to be sure to avoid conflicting with them so looking for the same wording but in our own. I'd also like to include our company logo, also attached in vector in horizontal and vertical for inclusion.

```html
<!DOCTYPE html>
<html lang="en">
<head>
<meta charset="utf-8">
<title>Bi-Lingual Recycling Sign</title>
<link href="https://fonts.googleapis.com/css2?family=Roboto:wght@500;700;900&family=Roboto+Condensed:wght@400;500;700&display=swap" rel="stylesheet">
<style>
:root{
  --maroon:#6b2340;
  --band:#561a2e;
  --band-grey:#dedede;
  --rule-grey:#cfcfcf;
  --paper:#ffffff;
  --chip:#ececec;
  --icon:#2a1a20;
  --bin-light:#f0c534;
  --bin-dark:#dcad22;
}
*{margin:0;padding:0;box-sizing:border-box}
html,body{width:1200px;height:857px;overflow:hidden;background:var(--paper)}
.sign{position:relative;width:1200px;height:857px;background:var(--paper);font-family:"Roboto",Arial,sans-serif;color:var(--maroon)}
.center{position:absolute;transform:translateX(-50%);text-align:center;white-space:nowrap}
.brand{position:absolute;top:56px;left:594px;transform:translateX(-50%);display:flex;align-items:center;gap:12px}
.brand__mark{width:24px;height:40px;background:var(--maroon)}
.brand__name{font-weight:500;font-size:28px;letter-spacing:1px;color:var(--maroon);line-height:1}
.headline{font-family:"Roboto Condensed",sans-serif;font-weight:700;font-size:70px;letter-spacing:0;line-height:1}
.notice{font-weight:700;font-size:26px;line-height:33px}
.band-grey{position:absolute;left:0;top:293px;width:1200px;height:65px;background:var(--band-grey)}
.band-title{top:311px;font-family:"Roboto Condensed",sans-serif;font-weight:500;font-size:27px;color:var(--maroon);line-height:30px}
.band-maroon{position:absolute;left:0;top:358px;width:1200px;height:326px;background:var(--band)}
.rule{position:absolute;left:0;top:684px;width:1200px;height:7px;background:var(--rule-grey)}
.list-title{top:388px;font-family:"Roboto Condensed",sans-serif;font-size:19px;color:#fff;letter-spacing:.3px}
.material{position:absolute;width:110px;transform:translateX(-50%);text-align:center}
.material__chip{width:64px;height:64px;border-radius:50%;background:var(--chip);margin:0 auto;display:flex;align-items:center;justify-content:center;box-shadow:0 0 0 3px rgba(0,0,0,.15)}
.material__chip svg{width:36px;height:36px;fill:none;stroke:var(--icon);stroke-width:2;stroke-linejoin:round;stroke-linecap:round}
.material__label{margin-top:12px;font-family:"Roboto Condensed",sans-serif;font-size:15px;color:#fff;white-space:nowrap}
.bin-art{position:absolute;left:420px;top:136px;width:369px;height:638px;border-radius:14px 14px 36px 36px;background:linear-gradient(90deg,var(--bin-dark),var(--bin-light) 50%,var(--bin-dark))}
.closing-small{font-weight:700;font-size:25px;line-height:28px}
.closing-big{font-weight:700;font-size:31px;line-height:34px}
.url{top:800px;left:607px;font-weight:700;font-size:24px}
</style>
</head>
<body>
<main class="sign">
  <div class="band-grey"></div>
  <div class="band-maroon"></div>
  <div class="rule"></div>

  <div class="brand"><span class="brand__mark"></span><span class="brand__name">ASHWORTH MANAGEMENT</span></div>

  <h1 class="center headline" style="left:217px;top:112px">RECYCLE</h1>
  <p class="center notice" style="left:217px;top:206px">NO PLASTIC BAGS<br>ACCEPTED</p>
  <h1 class="center headline" style="left:980px;top:112px" lang="es">RECICLAR</h1>
  <p class="center notice" style="left:980px;top:200px" lang="es">NO SE ACEPTAN<br>BOLSAS PLÁSTICAS</p>

  <p class="center band-title" style="left:226px">SINGLE SORT RECYCLING</p>
  <p class="center band-title" style="left:977px" lang="es">RECICLAJE DE CLASE ÚNICA</p>

  <p class="center list-title" style="left:217px">ACCEPTED MATERIALS</p>
  <p class="center list-title" style="left:976px" lang="es">ÚNICO ORDENAR EL RECICLAJE</p>

  <svg width="0" height="0" style="position:absolute">
    <defs>
      <symbol id="i-glass" viewBox="0 0 36 36"><path d="M9 5h18l-2 10a7 7 0 0 1-14 0z M18 22v8 M12 31h12"/></symbol>
      <symbol id="i-tin" viewBox="0 0 36 36"><rect x="9" y="5" width="18" height="26"/><path d="M9 9h18 M9 27h18"/><ellipse cx="18" cy="18" rx="5" ry="3"/></symbol>
      <symbol id="i-alu" viewBox="0 0 36 36"><rect x="7" y="8" width="17" height="22"/><path d="M24 10l6 2-6 18"/><path d="M11 23l2-8 2 8 M12 20h2 M18 15v6a2 2 0 0 0 4 0v-6"/></symbol>
      <symbol id="i-plastic" viewBox="0 0 36 36"><path d="M8 31v-14l3-4v-4h4v4l3 4v14z M22 31v-10h8v10z M24 21v-3h4v3 M11 9h4"/></symbol>
      <symbol id="i-box" viewBox="0 0 36 36"><path d="M18 12l12 5-12 5-12-5z M6 17v9l12 6 12-6v-9 M18 22v10 M6 17l-2-5 12-5 2 5 M30 17l2-5-12-5"/></symbol>
      <symbol id="i-paper" viewBox="0 0 36 36"><path d="M8 6h12v16h-12z M14 12h12v16h-12z M20 18h10v13h-10z"/></symbol>
      <symbol id="i-news" viewBox="0 0 36 36"><path d="M10 6h20v24h-22a3 3 0 0 1-3-3v-16h5z M10 11v16 M14 11h12v5h-12z M14 20h12 M14 24h12"/></symbol>
      <symbol id="i-mag" viewBox="0 0 36 36"><path d="M4 8h12a2 2 0 0 1 2 2v20a2 2 0 0 0-2-2h-12z M32 8h-12a2 2 0 0 0-2 2v20a2 2 0 0 1 2-2h12z M7 13h8 M7 17h8 M7 21h8 M21 13h8 M21 17h8 M21 21h8"/></symbol>
    </defs>
  </svg>

  <div class="material" style="left:76px;top:437px"><div class="material__chip"><svg><use href="#i-glass"/></svg></div><p class="material__label">GLASS</p></div>
  <div class="material" style="left:176px;top:437px"><div class="material__chip"><svg><use href="#i-tin"/></svg></div><p class="material__label">TIN</p></div>
  <div class="material" style="left:276px;top:437px"><div class="material__chip"><svg><use href="#i-alu"/></svg></div><p class="material__label">ALUMINUM</p></div>
  <div class="material" style="left:376px;top:437px"><div class="material__chip"><svg><use href="#i-plastic"/></svg></div><p class="material__label">PLASTIC (1-7)</p></div>
  <div class="material" style="left:76px;top:559px"><div class="material__chip"><svg><use href="#i-box"/></svg></div><p class="material__label">CARDBOARD</p></div>
  <div class="material" style="left:176px;top:559px"><div class="material__chip"><svg><use href="#i-paper"/></svg></div><p class="material__label">MIXED PAPER</p></div>
  <div class="material" style="left:276px;top:559px"><div class="material__chip"><svg><use href="#i-news"/></svg></div><p class="material__label">NEWSPAPERS</p></div>
  <div class="material" style="left:376px;top:559px"><div class="material__chip"><svg><use href="#i-mag"/></svg></div><p class="material__label">MAGAZINES</p></div>

  <div class="material" style="left:826px;top:437px" lang="es"><div class="material__chip"><svg><use href="#i-glass"/></svg></div><p class="material__label">VIDRIOS</p></div>
  <div class="material" style="left:927px;top:437px" lang="es"><div class="material__chip"><svg><use href="#i-tin"/></svg></div><p class="material__label">HOJALATA</p></div>
  <div class="material" style="left:1027px;top:437px" lang="es"><div class="material__chip"><svg><use href="#i-alu"/></svg></div><p class="material__label">ALUMINIO</p></div>
  <div class="material" style="left:1126px;top:437px" lang="es"><div class="material__chip"><svg><use href="#i-plastic"/></svg></div><p class="material__label">PLÁSTICO (1-7)</p></div>
  <div class="material" style="left:826px;top:559px" lang="es"><div class="material__chip"><svg><use href="#i-box"/></svg></div><p class="material__label">CARTÓN</p></div>
  <div class="material" style="left:927px;top:559px" lang="es"><div class="material__chip"><svg><use href="#i-paper"/></svg></div><p class="material__label">PAPEL</p></div>
  <div class="material" style="left:1027px;top:559px" lang="es"><div class="material__chip"><svg><use href="#i-news"/></svg></div><p class="material__label">PERIÓDICOS</p></div>
  <div class="material" style="left:1126px;top:559px" lang="es"><div class="material__chip"><svg><use href="#i-mag"/></svg></div><p class="material__label">REVISTAS</p></div>

  <div class="bin-art" role="img" aria-label="Illustration of a yellow wheeled recycling bin with a recycling symbol on its front"></div>

  <div class="center" style="left:217px;top:720px"><p class="closing-small">ABSOLUTELY</p><p class="closing-big">NO GARBAGE!</p></div>
  <div class="center" style="left:980px;top:716px" lang="es"><p class="closing-small">ABSOLUTAMENTE</p><p class="closing-big">NINGUNA BASURA!</p></div>

  <p class="center url">ashworthprop.com</p>
</main>
</body>
</html>
```